Startup photography business has a new logo, now we need business cards

Design a business card for the two partners of our business.
Our business Brisk Pelican has a new logo and we need to design a business card to showcase it and us.
Our colours of blue and orange are punchy and vivid, but how can we make the most of it on our card?

It should have our name Brisk Pelican
name of partner
phone number
email
website

Industry/Entity Type

Professional Photography

Contact Information for Business Card

Tom Ashworth
+61 400 55 61 72
tom@briskpelican.com.au
briskpelican.com.au

second card
Neil Porter
+61 400 918 263
neil@briskpelican.com.au
briskpelican.com.au

Colors
f37122
f68d4c
33a6d7
0592cd

Requirements
Must have
• one version of our logo, we have included options
• Name
• phone number
• email
• website
Nice to have
• instagram briskpelicanmedia
• twitter briskpelicanmedia
• facebook briskpelicanmedia

```html
<!DOCTYPE html>
<html lang="en">
<head>
<meta charset="utf-8">
<title>Brisk Pelican – Business Card</title>
<link rel="stylesheet" href="https://fonts.googleapis.com/css2?family=Open+Sans:wght@400;600;700&display=swap">
<style>
  :root {
    --page: #2b2b2d;
    --card: #050506;
    --orange: #f37122;
    --blue: #33a6d7;
    --blue-bright: #29b8ea;
    --shade: #0c2935;
  }
  * { margin: 0; padding: 0; box-sizing: border-box; }
  html, body { width: 1200px; height: 900px; overflow: hidden; }
  body {
    background: var(--page);
    font-family: "Open Sans", Arial, sans-serif;
    position: relative;
  }
  .card {
    position: absolute;
    left: 250px;
    width: 700px;
    height: 400px;
    background: var(--card);
    overflow: hidden;
    box-shadow: 0 18px 40px rgba(0,0,0,0.55);
  }
  .card--back { top: 35px; }
  .card--front { top: 465px; }
  .card svg.shapes { position: absolute; inset: 0; width: 100%; height: 100%; }

  .brand {
    position: absolute;
    display: flex;
    align-items: center;
    gap: 12px;
    font-weight: 700;
    color: var(--blue-bright);
    letter-spacing: 0.5px;
  }
  .brand__dot {
    width: 46px; height: 46px;
    border-radius: 50%;
    background: var(--orange);
    flex: none;
  }
  .card--back .brand { top: 110px; left: 390px; font-size: 34px; }
  .card--front .brand { top: 80px; left: 60px; font-size: 30px; }

  .social {
    position: absolute;
    right: 24px; top: 318px;
    display: flex; gap: 10px;
  }
  .social span {
    width: 16px; height: 16px;
    border-radius: 50%;
    background: #ffffff;
  }

  .person {
    position: absolute;
    right: 60px; top: 205px;
    font-size: 26px;
    font-weight: 700;
    letter-spacing: 0.5px;
    color: var(--blue-bright);
  }
  .person__last { color: var(--orange); }

  .contact {
    position: absolute;
    left: 60px; top: 252px;
    list-style: none;
    font-size: 16px;
    line-height: 22px;
    color: var(--blue-bright);
  }
  .contact li { display: flex; align-items: center; gap: 12px; }
  .contact svg { width: 12px; height: 12px; flex: none; }
</style>
</head>
<body>

<section class="card card--back" aria-label="Card back">
  <svg class="shapes" viewBox="0 0 700 400" aria-hidden="true">
    <circle cx="210" cy="185" r="165" fill="var(--shade)"/>
    <polygon points="0,378 555,378 548,392 0,392" fill="var(--orange)"/>
    <polygon points="575,336 700,336 700,392 555,392" fill="var(--blue-bright)"/>
  </svg>
  <div class="brand"><span class="brand__dot"></span>Brisk Pelican</div>
  <div class="social" aria-label="Social media: briskpelicanmedia">
    <span></span><span></span><span></span>
  </div>
</section>

<section class="card card--front" aria-label="Card front">
  <svg class="shapes" viewBox="0 0 700 400" aria-hidden="true">
    <circle cx="520" cy="150" r="170" fill="var(--shade)"/>
    <line x1="240" y1="236" x2="440" y2="216" stroke="var(--blue)" stroke-width="1.5"/>
    <line x1="440" y1="216" x2="700" y2="216" stroke="var(--blue)" stroke-width="1.5"/>
    <line x1="0" y1="236" x2="240" y2="236" stroke="var(--blue)" stroke-width="1.5"/>
    <polygon points="0,330 420,330 380,400 0,400" fill="var(--orange)"/>
    <polygon points="430,372 700,340 700,362 412,400 395,400" fill="var(--blue-bright)"/>
  </svg>
  <div class="brand"><span class="brand__dot"></span>Brisk Pelican</div>
  <div class="person">TOM <span class="person__last">ASHWORTH</span></div>
  <ul class="contact">
    <li>
      <svg viewBox="0 0 12 12"><path d="M2 1l2 0 1 3-1.5 1a6 6 0 0 0 3.5 3.5L8 7l3 1v2a1 1 0 0 1-1 1A9 9 0 0 1 1 2a1 1 0 0 1 1-1z" fill="var(--orange)"/></svg>
      +61 400 55 61 72
    </li>
    <li>
      <svg viewBox="0 0 12 12"><rect x="1" y="2.5" width="10" height="7" fill="none" stroke="var(--orange)" stroke-width="1.3"/><path d="M1 2.5l5 4 5-4" fill="none" stroke="var(--orange)" stroke-width="1.3"/></svg>
      tom@briskpelican.com.au
    </li>
    <li>
      <svg viewBox="0 0 12 12"><circle cx="6" cy="6" r="5" fill="none" stroke="var(--orange)" stroke-width="1.3"/><path d="M1 6h10M6 1c-2.5 3-2.5 7 0 10M6 1c2.5 3 2.5 7 0 10" fill="none" stroke="var(--orange)" stroke-width="1"/></svg>
      www.briskpelican.com.au
    </li>
  </ul>
</section>

</body>
</html>
```